Tending the long season

I am looking for a designer to provide me with a design or a re-design of my current book cover.

The book is about how I have supported Varenian Champions to success by applying science to their progress. You can see how it currently looks with a symbol representing the ‘champion’ being ‘supported by others’. While I like the current concept the overall design, including the words, my name and image is a bit amateur. I would be open to other ideas, particularly a more simplistic and eye-catching design. I would like the cover to have bold colours such as reds and yellows (I would need to know these colours for creation of the back cover.

If there is a symbol that is used on the book I will need the image as a png with a transparent background.

Thanks
Marek

```html
<!DOCTYPE html>
<html lang="en">
<head>
<meta charset="utf-8">
<title>Tending the long season — Book Cover</title>
<link href="https://fonts.googleapis.com/css2?family=Cinzel:wght@500&family=Jost:ital,wght@0,400;0,600;0,700;1,400&family=Oswald:wght@600&display=swap" rel="stylesheet">
<style>
  :root {
    --backdrop: #141414;
    --paper: #ffffff;
    --ink: #121626;
    --red: #e8202a;
    --mint: #3fe0a6;
    --mint-soft: #c9f1e6;
    --band: #0f1630;
    --band-text: #f4f4f4;
  }
  * { box-sizing: border-box; margin: 0; padding: 0; }
  html, body {
    width: 1200px; height: 670px; overflow: hidden;
    background: var(--backdrop);
  }
  .book-cover {
    position: absolute;
    left: 411px; top: 56px;
    width: 378px; height: 558px;
    background: linear-gradient(to bottom,
      var(--paper) 0px, var(--paper) 328px,
      var(--mint-soft) 420px, var(--mint) 502px);
    overflow: hidden;
  }
  .kicker-row {
    position: absolute; left: 0; right: 0; top: 10px;
    display: flex; align-items: center; gap: 14px;
  }
  .kicker-rule { flex: 1; height: 2px; background: var(--ink); }
  .kicker {
    font-family: "Jost", sans-serif; font-weight: 400; font-style: italic;
    font-size: 24px; line-height: 26px; letter-spacing: 1px;
    color: var(--red);
  }
  .title-line {
    position: absolute; left: 0; right: 0; text-align: center;
    color: var(--ink);
    font-family: "Jost", sans-serif; font-weight: 700;
    font-size: 48px; line-height: 1; top: 36px; letter-spacing: 0.5px;
  }
  .title-main {
    position: absolute; left: 0; right: 0; text-align: center;
    color: var(--red);
    font-family: "Oswald", sans-serif; font-weight: 600;
    font-size: 92px; line-height: 1; top: 80px; letter-spacing: 2px;
  }
  .subtitle {
    position: absolute; left: 0; right: 0; top: 176px; text-align: center;
    font-family: "Jost", sans-serif; font-weight: 400;
    font-size: 16px; line-height: 20px; color: var(--ink);
  }
  .subtitle strong { font-weight: 600; }
  .subtitle .accent { color: var(--red); font-weight: 700; }
  .hero-art {
    position: absolute; left: 16px; top: 256px;
    width: 346px; height: 160px;
    border-radius: 6px;
    background: linear-gradient(to right,
      #e8312f 0%, #2f8fe0 28%, #22b34a 52%, #f06a1c 76%, #f6b81c 100%);
    opacity: 0.85;
  }
  .author-band {
    position: absolute; left: 0; right: 0; bottom: 0; height: 56px;
    background: var(--band);
    display: flex; align-items: center; justify-content: center;
    font-family: "Cinzel", serif; font-weight: 500;
    font-size: 28px; letter-spacing: 2px; color: var(--band-text);
  }
</style>
</head>
<body>
  <main class="book-cover">
    <div class="kicker-row">
      <span class="kicker-rule"></span>
      <span class="kicker">TENDING</span>
      <span class="kicker-rule"></span>
    </div>
    <h1>
      <span class="title-line">THE LONG</span>
      <span class="title-main">SEASON</span>
    </h1>
    <p class="subtitle">The <strong>Craft of Using Evidence</strong><br>for the <span class="accent">FINEST RUNNER</span></p>
    <div class="hero-art" role="img" aria-label="Watercolour silhouettes of five runners in red, blue, green, orange and yellow, striding in a row"></div>
    <footer class="author-band">MAREK HALVORSEN</footer>
  </main>
</body>
</html>
```